Startup that helps high growth companies expand to new office locations needs a polished website

Hello! We are a B2B startup helping fast growing companies expand to new office locations. We are in need of a polished, vibrant website that is modern and professional. Our mission is to accelerate tech-enabled economic opportunity beyond silicon valley.
- Our current site is: https://www.tandivo.co
- We help companies in 3 steps: Discover, Expand, Align
- Discover = analysis on where a company should expand to
geographically
- Expand = manage the entire office build out process
- Align = ongoing support at the new office and help culturally aligning
new office to HQ
- Look through our deck which is attached in this brief and incorporate parts of our deck into the website, especially content and messaging! Slide 2 in particular is important, so I've taken a screenshot of it individually and attached it.
- Please also carefully read through our branding document which includes color palettes and examples of websites we like. However, we are open to any ideas you think are better in terms of color and font! https://slides.marquenta-files.net/deck/7Qm2Lx9Pa4RtZk3Nw8Vb5Hc6Jd1Fg0Sy/edit#slide=id.k7m2p9x4r1_0_0
- We need a strong call to action for customers to contact us

We are also looking for a new logo! This logo should convey that we help companies expand beyond their current office locations.

Thanks! Looking forward to seeing your designs!

Target Market(s)

hypergrowth startups of 100-500 people

Logo Text

Tandivo

Coding

Coded - Design and coding required

Number of Pages Required

2 page

Font styles to use
Sans Serif

Requirements
Must have
• - Clear call to action on landing page
• - A separate about us page. Please refer to the wireframe attached
• - Incorporate content from the current homepage at https://www.tandivo.co/ (Discover, Expand, Align content, which are the 3 pieces of our offering)
• - Incorporate messaging in Slide 2 of attached company ppt. I've also taken a screenshot of it individually and attached it.
• - Testimonials sections on homepage
Nice to have
• - Incorporate other elements of the slide deck as you see fit

```html
<!DOCTYPE html>
<html lang="en">
<head>
<meta charset="utf-8">
<title>Tandivo — Expansion Ops Concierge</title>
<link href="https://fonts.googleapis.com/css2?family=Raleway:wght@300;400;600;700&family=Open+Sans:wght@400;600;700&display=swap" rel="stylesheet">
<style>
:root{
  --blue:#2f8fe8;
  --blue-deep:#1c6fd1;
  --blue-light:#5fb0f5;
  --navy:#1d3557;
  --ink:#333a44;
  --muted:#7a828d;
  --line:#dfe6ee;
  --pale:#f4f7fb;
  --white:#ffffff;
  --dark:#1a1f27;
}
*{box-sizing:border-box;margin:0;padding:0}
html,body{width:1200px;height:5388px;overflow:hidden}
body{font-family:"Open Sans",Arial,sans-serif;color:var(--ink);background:var(--white);position:relative}
.section{position:absolute;left:0;width:1200px}
.h2{font-family:"Raleway",Arial,sans-serif;font-weight:300;font-size:44px;text-align:center;color:var(--ink)}
.h2 b{font-weight:700}
.lead{text-align:center;font-size:17px;color:var(--muted)}
.lead strong{color:var(--blue);font-weight:600}
.btn{display:inline-block;background:var(--blue);color:var(--white);font-size:13px;font-weight:600;letter-spacing:1px;padding:12px 26px;border-radius:3px;text-transform:uppercase}
.brand{font-family:"Raleway",Arial,sans-serif;font-weight:700;display:flex;align-items:center;gap:10px}
.brand i{display:block;border-radius:50%;background:currentColor}

/* hero */
.hero{top:0;height:608px;background:linear-gradient(135deg,#3d8fd6 0%,#2a6fba 55%,#1f5aa0 100%)}
.nav{position:absolute;top:40px;left:140px;right:140px;display:flex;align-items:center}
.nav .brand{color:var(--white);font-size:30px}
.nav .brand i{width:14px;height:14px}
.menu{display:flex;gap:26px;margin-left:auto;font-size:14px;color:var(--white);align-items:center}
.menu span{position:relative}
.menu .active{border-bottom:2px solid var(--white);padding-bottom:3px}
.dropdown{position:absolute;top:28px;left:-12px;background:var(--white);color:var(--ink);font-size:13px;padding:10px 16px;line-height:2;border-radius:2px;box-shadow:0 4px 12px rgba(0,0,0,.15)}
.nav .btn{margin-left:34px;font-size:12px;padding:11px 18px}
.hero-copy{position:absolute;top:250px;left:240px;display:flex;align-items:center;gap:26px;color:var(--white)}
.hero-copy h1{font-family:"Raleway",Arial,sans-serif;font-weight:700;font-size:84px;letter-spacing:2px}
.hero-copy p{font-family:"Raleway",Arial,sans-serif;font-size:30px;line-height:1.25;font-weight:600;text-transform:uppercase}
.hero .cta{position:absolute;top:372px;left:508px}

/* mission */
.mission{top:608px;height:812px}
.mission .h2{margin-top:80px}
.mission .lead{margin-top:26px}
.trends{position:absolute;top:290px;left:210px;width:780px;display:flex;justify-content:space-between}
.trend{width:220px;height:190px;background:var(--white);box-shadow:0 6px 24px rgba(30,60,100,.12);position:relative;padding:70px 24px 0;font-size:19px;line-height:1.35;color:var(--ink)}
.trend .ico{position:absolute;top:-36px;left:74px;width:72px;height:72px;border-radius:50%;background:var(--blue-deep)}
.mission .wires{position:absolute;top:480px;left:0}
.mission .hub{position:absolute;top:680px;left:0;width:1200px;text-align:center}
.mission .hub .brand{justify-content:center;color:var(--blue-deep);font-size:28px}
.mission .hub .brand i{width:12px;height:12px}
.mission .hub p{margin-top:14px;font-size:14px;color:var(--muted);line-height:1.5}

/* why */
.why{top:1420px;height:600px;background:linear-gradient(180deg,var(--blue-deep),var(--blue))}
.why .h2{color:var(--white);margin-top:70px}
.why .lead{color:#dbeafb;margin-top:18px;font-size:14px;line-height:1.5}
.why svg{position:absolute;top:0;left:0}
.why-note{position:absolute;width:190px;font-size:12px;line-height:1.5;color:#e6f1fd}
.why-core{position:absolute;top:405px;left:530px;width:140px;text-align:center;color:var(--blue-deep)}
.why-core .brand{justify-content:center;font-size:26px}
.why-core .brand i{width:10px;height:10px}
.why-core small{display:block;font-size:10px;color:var(--muted);margin-top:2px}

/* offering */
.offering{top:2020px;height:812px}
.offering .h2{margin-top:40px}
.offering .what{text-align:center;margin-top:26px;font-size:18px;color:var(--ink)}
.offering .lead{margin-top:14px}
.cards{position:absolute;top:290px;left:140px;width:920px;display:flex;justify-content:space-between}
.card{width:290px;height:440px;background:var(--white);border:1px solid var(--line);position:relative;padding:90px 30px 0;text-align:center}
.card.on{border:2px solid var(--blue);box-shadow:0 8px 28px rgba(47,143,232,.2)}
.card .ico{position:absolute;top:-40px;left:105px;width:80px;height:80px;border-radius:50%;background:var(--navy)}
.card.on .ico{background:var(--blue)}
.card h3{font-family:"Raleway",Arial,sans-serif;font-size:30px;font-weight:700;letter-spacing:1px;color:var(--ink)}
.card h4{font-size:16px;font-weight:400;color:var(--muted);margin-top:4px}
.card ul{list-style:none;text-align:left;margin-top:34px;font-size:12px;line-height:1.5;color:var(--muted)}
.card li{position:relative;padding-left:20px;margin-bottom:14px}
.card li:before{content:"";position:absolute;left:0;top:5px;width:8px;height:8px;border-radius:50%;background:var(--navy)}
.card.on li:before{background:var(--blue)}
.card .btn{position:absolute;bottom:26px;left:100px;background:var(--navy);font-size:11px;padding:8px 16px}
.card.on .btn{background:var(--blue)}

/* expand */
.expand{top:2832px;height:688px;background:linear-gradient(180deg,#3a9ef0,#2b85dd)}
.expand .h2{color:var(--white);margin-top:70px}
.company{position:absolute;top:180px;left:0;width:1200px;text-align:center;color:var(--white)}
.company .label{font-family:"Raleway",Arial,sans-serif;font-size:22px;font-weight:300;color:#cfe6fc}
.company .brand{justify-content:center;font-size:32px;margin-top:10px}
.company .brand i{width:12px;height:12px}
.company .brace{position:absolute;top:0;font-family:"Raleway",Arial,sans-serif;font-weight:300;font-size:110px;line-height:1;color:var(--white)}
.city{position:absolute}
.city.main{top:310px;left:320px;width:560px;height:300px;background:linear-gradient(180deg,#6f93c9 0%,#a7b9d8 40%,#7a6f8e 70%,#3b3f57 100%)}
.city.side{top:340px;width:160px;height:270px;background:linear-gradient(180deg,#7fa7d8,#3e5f8c)}
.city-name{position:absolute;color:var(--white);font-family:"Raleway",Arial,sans-serif;font-weight:600}
.arrow{position:absolute;top:450px;width:28px;height:28px}
.expand .caption{position:absolute;top:630px;left:0;width:1200px;text-align:center;font-size:12px;color:#dcecfc}

/* testimonials */
.testimonials{top:3520px;height:620px;background:linear-gradient(180deg,#2b3038,#15181d)}
.testimonials .h2{color:var(--white);margin-top:60px}
.testimonials .lead{color:#c2c8d0;margin-top:14px}
.quotes{position:absolute;top:205px;left:140px;width:920px;display:flex;justify-content:space-between}
.quote{width:440px;height:160px;border:1px solid rgba(255,255,255,.35);position:relative;padding:22px 26px 0 124px;color:#e4e8ee;font-size:13px;line-height:1.55}
.quote .avatar{position:absolute;top:40px;left:26px;width:76px;height:76px;border-radius:50%;background:linear-gradient(135deg,#9aa5b3,#5d6673)}
.quote .mark{position:absolute;top:14px;left:110px;font-family:Georgia,serif;font-size:36px;color:var(--white);line-height:1}
.quote cite{display:block;margin-top:14px;font-style:normal;font-size:13px}
.quote cite b{color:var(--white)}
.dots{position:absolute;top:535px;left:0;width:1200px;display:flex;justify-content:center;gap:9px}
.dots i{width:8px;height:8px;border-radius:50%;background:rgba(255,255,255,.4)}
.dots i:first-child{background:var(--white)}

/* team */
.team{top:4140px;height:880px;background:var(--pale)}
.team .h2{margin-top:60px}
.team .lead{margin-top:14px}
.members{position:absolute;top:180px;left:120px;width:960px;display:flex;justify-content:space-between}
.member{width:220px;text-align:center}
.member .photo{width:140px;height:140px;border-radius:50%;margin:0 auto;background:linear-gradient(135deg,#c9ced6,#6e7682)}
.member h5{font-size:16px;font-weight:700;color:var(--ink);margin-top:18px}
.member .role{font-size:13px;color:var(--muted);margin-top:2px}
.member p{font-size:11px;line-height:1.5;color:var(--muted);margin-top:10px}
.member.on h5{color:var(--blue)}
.origins{position:absolute;top:530px;left:150px;width:900px;height:200px;background:var(--white);box-shadow:0 6px 22px rgba(30,60,100,.08);text-align:center;padding-top:30px}
.origins h6{font-size:14px;font-weight:600;color:var(--ink)}
.origins .names{display:flex;justify-content:space-around;margin-top:44px;font-size:26px;font-weight:600;color:var(--muted)}

/* footer */
.footer{top:5020px;height:368px;background:var(--blue)}
.fcol{position:absolute;top:54px;color:var(--white)}
.fcol h6{font-family:"Raleway",Arial,sans-serif;font-size:18px;font-weight:400}
.fcol h6 b{font-weight:700}
.fcol ul{list-style:none;margin-top:20px;font-size:12px;line-height:2.2;color:#dbeafb}
.fcol p{font-size:12px;color:#dbeafb;line-height:1.5;margin-top:18px}
.field{margin-top:16px;width:230px;height:30px;border:1px solid rgba(255,255,255,.7);font-size:11px;color:#dbeafb;padding:7px 10px}
.footer .sub{margin-top:10px;background:var(--blue-deep);font-size:11px;padding:8px 18px}
.fbrand{position:absolute;top:60px;left:880px;color:var(--white)}
.fbrand .brand{font-size:32px}
.fbrand .brand i{width:12px;height:12px}
.social{display:flex;gap:8px;margin-top:22px}
.social i{width:26px;height:26px;border-radius:50%;border:1px solid var(--white)}
.copy{position:absolute;bottom:24px;left:0;width:1200px;text-align:center;font-size:11px;color:#cfe4fb}
</style>
</head>
<body>

<header class="section hero" role="img" aria-label="Aerial photo of a team working in a modern office, tinted blue">
  <nav class="nav">
    <div class="brand">Tandivo<i></i></div>
    <div class="menu">
      <span class="active">Home</span>
      <span>Mission</span>
      <span>Why Us</span>
      <span>Offering
        <span class="dropdown">Discover<br>Expand<br>Align</span>
      </span>
      <span>Team</span>
      <span>Blog</span>
    </div>
    <span class="btn">Request a Consultation</span>
  </nav>
  <div class="hero-copy">
    <h1>ARE YOU</h1>
    <p>Paying top dollar and<br>still losing talent?</p>
  </div>
  <span class="btn cta">We can help</span>
</header>

<section class="section mission">
  <h2 class="h2"><b>Our</b> Mission</h2>
  <p class="lead">Our mission is <strong>to accelerate tech-enabled economic opportunity</strong> beyond Silicon Valley.</p>
  <div class="trends">
    <div class="trend"><span class="ico"></span>Rise of Distributed Teams</div>
    <div class="trend"><span class="ico"></span>Emerging Tech Hubs Across the Country</div>
    <div class="trend"><span class="ico"></span>Proliferation of Space-as-a-Service</div>
  </div>
  <svg class="wires" width="1200" height="200" viewBox="0 0 1200 200" fill="none" stroke="#c7d3e0" stroke-width="2">
    <path d="M320 0 V110 H880 V0"/>
    <path d="M600 0 V180"/>
  </svg>
  <div class="hub">
    <div class="brand">Tandivo<i></i></div>
    <p>recognizes and leverages these<br>undeniable trends to be your turn-key office<br>expansion partner</p>
  </div>
</section>

<section class="section why">
  <svg width="1200" height="600" viewBox="0 0 1200 600" fill="none">
    <circle cx="600" cy="440" r="150" stroke="#ffffff" stroke-opacity=".6" stroke-width="2"/>
    <circle cx="600" cy="440" r="82" fill="#ffffff"/>
    <g fill="#4aa4f2" stroke="#ffffff" stroke-width="3">
      <circle cx="600" cy="290" r="20"/>
      <circle cx="470" cy="365" r="20"/>
      <circle cx="730" cy="365" r="20"/>
      <circle cx="470" cy="515" r="20"/>
      <circle cx="730" cy="515" r="20"/>
      <circle cx="600" cy="590" r="20"/>
    </g>
    <g stroke="#ffffff" stroke-opacity=".5">
      <path d="M390 370 H450"/><path d="M750 370 H810"/>
      <path d="M390 520 H450"/><path d="M750 520 H810"/>
    </g>
  </svg>
  <h2 class="h2">Why <b>Tandivo</b></h2>
  <p class="lead">We onboarded and scaled several successful<br>B2B SaaS startups from inception, & saw multiple large<br>expansion teams grow IPO</p>
  <p class="why-note" style="top:340px;left:190px;text-align:right">We led technical teams (sales, engineering, talent, and support)</p>
  <p class="why-note" style="top:340px;left:820px">We built units for firms from 10 to 600 employees.</p>
  <p class="why-note" style="top:495px;left:190px;text-align:right">We placed Fortune businesses on growth over the last decade.</p>
  <p class="why-note" style="top:495px;left:820px">We built and grew many international product teams for startups.</p>
  <div class="why-core">
    <div class="brand">Tandivo<i></i></div>
    <small>expansion ops concierge</small>
  </div>
</section>

<section class="section offering">
  <h2 class="h2">We <b>Offering</b></h2>
  <p class="what">What is <b>Tandivo?</b></p>
  <p class="lead">Your <strong>Expansion Ops Concierge</strong> with three key offerings for <strong>building effective distributed teams.</strong></p>
  <div class="cards">
    <article class="card on">
      <span class="ico"></span>
      <h3>DISCOVER</h3>
      <h4>Evaluate new geos</h4>
      <ul>
        <li>Intensive customer to define key drivers for new team location</li>
        <li>Conduct multidimensional analysis to identify geo climate, talent and market cost of living</li>
        <li>Secure and hire right leadership</li>
      </ul>
      <span class="btn">Read more</span>
    </article>
    <article class="card">
      <span class="ico"></span>
      <h3>EXPAND</h3>
      <h4>Set up new geo</h4>
      <ul>
        <li>Run centralized Expansion Playbook to set up remote office, including office space and vendors</li>
        <li>Serve as a single point of contact, managing all vendor relationships</li>
        <li>Manage project plan and updates</li>
      </ul>
      <span class="btn">Read more</span>
    </article>
    <article class="card">
      <span class="ico"></span>
      <h3>ALIGN</h3>
      <h4>Ensure success</h4>
      <ul>
        <li>Create Local Ops Concierge for ongoing growth needs</li>
        <li>Leverage onsite office insights for CPU &amp; C-suite</li>
        <li>Continuously refine Playbook</li>
      </ul>
      <span class="btn">Read more</span>
    </article>
  </div>
</section>

<section class="section expand">
  <h2 class="h2">Where Can We <b>Help You Expand?</b></h2>
  <div class="company">
    <span class="brace" style="left:470px">{</span>
    <span class="brace" style="left:705px">}</span>
    <div class="label">Your Company</div>
    <div class="brand">Tandivo<i></i></div>
  </div>
  <div class="city side" style="left:0" role="img" aria-label="City skyline photo of Eastmere"></div>
  <div class="city side" style="left:1040px" role="img" aria-label="City skyline photo of Pinecrest"></div>
  <div class="city main" role="img" aria-label="Photo of the Westhaven skyline with mountains behind"></div>
  <span class="city-name" style="top:460px;left:120px;font-size:18px;transform:rotate(-90deg)">Eastmere</span>
  <span class="city-name" style="top:460px;left:1020px;font-size:18px;transform:rotate(90deg)">Pinecrest</span>
  <span class="city-name" style="top:555px;left:345px;font-size:30px">Westhaven</span>
  <svg class="arrow" style="left:240px" viewBox="0 0 28 28" fill="none" stroke="#ffffff" stroke-width="3"><path d="M18 4 L8 14 L18 24"/></svg>
  <svg class="arrow" style="left:932px" viewBox="0 0 28 28" fill="none" stroke="#ffffff" stroke-width="3"><path d="M10 4 L20 14 L10 24"/></svg>
  <p class="caption">Mid-tier talent, abundant startups and an affordable cost of living. Westhaven<br>offers deep talent pools at friendly rates.</p>
</section>

<section class="section testimonials" role="img" aria-label="Dimmed photo of a team in a meeting">
  <h2 class="h2">Client <b>Testimonials</b></h2>
  <p class="lead">Some of our Happy Clients</p>
  <div class="quotes">
    <blockquote class="quote">
      <span class="avatar" role="img" aria-label="Client portrait"></span>
      <span class="mark">&ldquo;</span>
      Working with the team made our new hub feel like home within weeks. They handled leases, vendors and hiring so we could stay focused on the product.
      <cite><b>&mdash; Elian Varga</b> Business Executive</cite>
    </blockquote>
    <blockquote class="quote">
      <span class="avatar" role="img" aria-label="Client portrait"></span>
      <span class="mark">&ldquo;</span>
      Their playbook took the guesswork out of choosing a second city. Our remote office opened on time and the culture stayed aligned with HQ.
      <cite><b>&mdash; Noor Whitcombe</b> Business Executive</cite>
    </blockquote>
  </div>
  <div class="dots"><i></i><i></i><i></i><i></i><i></i><i></i></div>
</section>

<section class="section team">
  <h2 class="h2"><b>Our</b> Team</h2>
  <p class="lead">Startup Operators With <strong>Decades of Growth Experience</strong></p>
  <div class="members">
    <div class="member">
      <div class="photo" role="img" aria-label="Portrait of Mirela Costan"></div>
      <h5>Mirela Costan</h5>
      <div class="role">Head of Operations</div>
      <p>15+ years leading workforce expansion &amp; workspace strategy for companies from 100 to 1000s of employees.</p>
    </div>
    <div class="member on">
      <div class="photo" role="img" aria-label="Portrait of Junie Park"></div>
      <h5>Junie Park</h5>
      <div class="role">Product Lead</div>
      <p>Product at B2B SaaS startups. Experience growing multiple startups into remote teams in a product-focused environment.</p>
    </div>
    <div class="member">
      <div class="photo" role="img" aria-label="Portrait of Rohan Valdi"></div>
      <h5>Rohan Valdi</h5>
      <div class="role">CEO</div>
      <p>Co-founder/CEO at 3 startups. 15+ years B2B SaaS.</p>
    </div>
    <div class="member">
      <div class="photo" role="img" aria-label="Portrait of Tobin Hale"></div>
      <h5>Tobin Hale</h5>
      <div class="role">Co-Founder, Advisor</div>
      <p>Co-Founder, village fund. Extensive investment and startup innovation experience. Computer Science.</p>
    </div>
  </div>
  <div class="origins">
    <h6>Where We've Come From</h6>
    <div class="names">
      <span>Lumenforge</span><span>wellquarry</span><span>boxgrove</span><span>Sentrova</span><span>PIVOTA</span>
    </div>
  </div>
</section>

<footer class="section footer">
  <div class="fcol" style="left:140px">
    <h6><b>Quick</b> Links</h6>
    <ul><li>Home</li><li>Mission</li><li>Why Us</li><li>Offering</li><li>Team</li><li>Blog</li></ul>
  </div>
  <div class="fcol" style="left:330px">
    <h6><b>Contact</b> Details</h6>
    <p>Tandivo<br>1201 Harrowgate Avenue<br>Suite 4, Fairlow, CA 94000</p>
    <p>(555) 014-7782</p>
    <p>hello@tandivo.co</p>
  </div>
  <div class="fcol" style="left:580px">
    <h6>Newsletter <b>Signup</b></h6>
    <p>Subscribe for news and updates<br>on our latest expansions.</p>
    <div class="field">Enter your email</div>
    <span class="btn sub">Subscribe</span>
  </div>
  <div class="fbrand">
    <div class="brand">Tandivo<i></i></div>
    <div class="social"><i></i><i></i><i></i><i></i><i></i><i></i></div>
  </div>
  <p class="copy">Copyright 2019 Tandivo Inc. All Rights Reserved.</p>
</footer>

</body>
</html>
```